Marigold Finch Lending Solutions business card design

Need a business card design for my mortgage broking business Marigold Finch Lending Solutions.

Target Market(s)

Mortgage clients/colleagues

Industry/Entity Type

Business

Requirements
Must have
• Must utilise logo attached. Possibly have logo only on back of card. my name & contact details on front and something creative?

Must incorporate purple/black/white in colour scheme.

Must incorporate tag line 'The Home Loan Sleuths' under logo - using a script style fint. UPDATE: Mistral doesn't seem to be working on the card. Happy for you to try a different font. preferably a script style font.

Standard business card size.
Nice to have
• Try and incorporate the detective theme - but keep it looking sharp and professional.
Have attached some sample designs - does not have to be this - happy to review any ideas you may have.

```html
<!DOCTYPE html>
<html lang="en">
<head>
<meta charset="utf-8">
<title>Marigold Finch Lending Solutions – Business Card</title>
<link rel="stylesheet" href="https://fonts.googleapis.com/css2?family=Open+Sans:wght@400;600&display=swap">
<style>
  :root {
    --backdrop: #e4e2df;
    --card-white: #f4f4f4;
    --card-black: #1c1c1c;
    --card-black-edge: #0b0b0b;
    --purple: #7a2a82;
    --purple-soft: #9a4fa2;
    --ink: #4a4a4a;
    --ink-soft: #6b6b6b;
    --logo-white: #ffffff;
  }
  * { box-sizing: border-box; margin: 0; padding: 0; }
  html, body {
    width: 1200px; height: 900px; overflow: hidden;
    background: var(--backdrop);
    font-family: "Open Sans", Arial, sans-serif;
  }
  .canvas {
    width: 1200px; height: 900px;
    display: flex; flex-direction: column;
    align-items: center; justify-content: center; gap: 60px;
  }
  .card {
    position: relative;
    width: 600px; height: 343px;
    border-radius: 6px;
    box-shadow: 0 10px 28px rgba(0,0,0,.22);
    overflow: hidden;
  }

  /* Back of card */
  .card--back {
    background: radial-gradient(ellipse at 50% 35%, #343434 0%, var(--card-black) 55%, var(--card-black-edge) 100%);
    display: flex; flex-direction: column; align-items: center; justify-content: center;
  }
  .brand-name {
    color: var(--logo-white);
    font-weight: 600;
    font-size: 28px;
    line-height: 1.2;
    text-align: center;
    letter-spacing: .5px;
  }
  .tagline {
    margin-top: 30px;
    color: var(--purple-soft);
    font-size: 13px;
    letter-spacing: 6px;
    text-transform: uppercase;
  }

  /* Front of card */
  .card--front { background: linear-gradient(160deg, #fafafa 0%, var(--card-white) 60%, #e9e9e9 100%); }
  .fingerprint {
    position: absolute; left: 32px; top: 38px;
    width: 48px; height: 62px;
    border-radius: 50% 50% 46% 46%;
    background: radial-gradient(ellipse at 50% 50%, #b5b5b5 0%, #8e8e8e 60%, #c8c8c8 100%);
    opacity: .75;
  }
  .holder { position: absolute; left: 92px; top: 30px; }
  .holder__name { color: var(--purple); font-size: 28px; font-weight: 400; line-height: 1.2; }
  .holder__role { color: var(--ink-soft); font-size: 13px; line-height: 1.35; margin-top: 4px; }

  .contact { position: absolute; left: 330px; top: 178px; color: var(--ink); font-size: 13.5px; font-style: normal; }
  .contact__row { display: flex; align-items: flex-start; gap: 14px; margin-bottom: 14px; }
  .contact__row:last-child { margin-bottom: 0; }
  .contact__icon { width: 16px; height: 16px; flex: none; margin-top: 2px; fill: var(--purple); }
  .contact__text { line-height: 1.35; }
  .website {
    position: absolute; left: 32px; bottom: 30px;
    color: var(--purple); font-size: 13.5px;
  }
</style>
</head>
<body>
<main class="canvas">

  <section class="card card--back" aria-label="Card back">
    <p class="brand-name">Marigold Finch<br>Lending Solutions</p>
    <p class="tagline">The Home Loan Sleuths</p>
  </section>

  <section class="card card--front" aria-label="Card front">
    <div class="fingerprint" role="img" aria-label="Grey fingerprint motif"></div>
    <div class="holder">
      <h1 class="holder__name">Clara Whitmore</h1>
      <p class="holder__role">Managing Director<br>Non-Conforming Mortgage Specialist</p>
    </div>

    <address class="contact">
      <div class="contact__row">
        <svg class="contact__icon" viewBox="0 0 16 16" aria-hidden="true"><path d="M8 0a5.5 5.5 0 0 0-5.5 5.5C2.5 9.6 8 16 8 16s5.5-6.4 5.5-10.5A5.5 5.5 0 0 0 8 0zm0 7.8a2.3 2.3 0 1 1 0-4.6 2.3 2.3 0 0 1 0 4.6z"/></svg>
        <span class="contact__text">Harbour House, Level 1<br>218 Wren Lane<br>Melbourne 3000</span>
      </div>
      <div class="contact__row">
        <svg class="contact__icon" viewBox="0 0 16 16" aria-hidden="true"><path d="M4.5 0h7A1.5 1.5 0 0 1 13 1.5v13a1.5 1.5 0 0 1-1.5 1.5h-7A1.5 1.5 0 0 1 3 14.5v-13A1.5 1.5 0 0 1 4.5 0zM5 2v10h6V2zm3 11a1 1 0 1 0 0 2 1 1 0 0 0 0-2z"/></svg>
        <span class="contact__text">0400 512 368</span>
      </div>
      <div class="contact__row">
        <svg class="contact__icon" viewBox="0 0 16 16" aria-hidden="true"><path d="M0 3h16v1.2L8 9 0 4.2zm0 2.6 8 4.8 8-4.8V13H0z"/></svg>
        <span class="contact__text">clara@marigoldloans.com.au</span>
      </div>
    </address>

    <p class="website">www.marigoldloans.com.au</p>
  </section>

</main>
</body>
</html>
```